promotional flyer for Veltrano Gym

we are after a double sided a5 leaflet to promote our gym, this is to go out to the general public to entice them into getting membership.

gym membership is £30 per month

it should also include the offer of - if you present this leaflet then there will be no joining fee

some of the features of the gym include

strength machines
cardio machines
functional area
sprung floor mat area

Target Market(s)

Adults 16+ who want to go to the gym and workout

Industry/Entity Type

Gym

Font styles to use
Other font styles liked:
• montserrat Regular

Requirements
Must have
• Clean on brand design
• use images supplied by us
Nice to have
• focus on an inclusive experience as the gym will be advertised to everyone
• should also use our "fitter, stronger, Healthier"

```html
<!DOCTYPE html>
<html lang="en">
<head>
<meta charset="UTF-8">
<title>Veltrano Gym – Membership Flyer</title>
<link href="https://fonts.googleapis.com/css2?family=Montserrat:wght@300;400;600;800;900&display=swap" rel="stylesheet">
<style>
  :root {
    --slate: #56616a;
    --slate-soft: #6f777f;
    --orange: #e4572a;
    --orange-light: #f19b63;
    --orange-pale: #f5b485;
    --red: #e3261a;
    --photo-dark: #a83a1f;
    --photo-mid: #d3602f;
    --photo-light: #ee9a6a;
    --paper: #ffffff;
  }
  * { margin: 0; padding: 0; box-sizing: border-box; }
  html, body { width: 927px; height: 1200px; overflow: hidden; background: var(--paper); }
  .flyer {
    position: relative;
    width: 927px;
    height: 1200px;
    background: var(--paper);
    font-family: "Montserrat", sans-serif;
    overflow: hidden;
  }
  .artwork { position: absolute; inset: 0; }

  .brand {
    position: absolute;
    top: 49px;
    left: 0;
    width: 522px;
    text-align: center;
  }
  .brand-ring {
    display: block;
    margin: 0 auto;
    width: 114px;
    height: 114px;
    border: 5px solid var(--slate);
    border-radius: 50%;
  }
  .brand-name {
    margin-top: 23px;
    font-weight: 400;
    font-size: 40px;
    letter-spacing: 7px;
    color: var(--slate);
    line-height: 1;
    text-transform: uppercase;
  }
  .brand-tagline {
    margin-top: 17px;
    font-weight: 600;
    font-size: 15px;
    letter-spacing: 3px;
    color: var(--orange);
    text-transform: uppercase;
  }

  .price-badge {
    position: absolute;
    left: 551px;
    top: 847px;
    width: 318px;
    height: 318px;
    border: 5px solid var(--slate);
    border-radius: 50%;
    text-align: center;
    color: var(--slate);
    text-transform: uppercase;
  }
  .price-title {
    margin-top: 28px;
    font-weight: 900;
    font-size: 70px;
    line-height: 1;
    letter-spacing: -1px;
  }
  .price-subtitle {
    font-weight: 800;
    font-size: 23px;
    line-height: 1;
    margin-top: 2px;
    letter-spacing: -0.5px;
  }
  .price-amount {
    font-weight: 900;
    font-size: 124px;
    line-height: 1;
    color: var(--orange);
    letter-spacing: -3px;
    margin-top: 2px;
  }
  .price-period {
    font-weight: 800;
    font-size: 25px;
    line-height: 1;
    margin-top: 8px;
    letter-spacing: -0.5px;
  }

  .offer {
    position: absolute;
    left: 66px;
    top: 1098px;
    padding-left: 31px;
    border-left: 14px solid var(--orange);
    color: var(--slate);
    font-weight: 400;
    font-size: 16.5px;
    line-height: 30px;
    text-transform: uppercase;
    letter-spacing: 0.3px;
  }
</style>
</head>
<body>
<main class="flyer">
  <svg class="artwork" width="927" height="1200" viewBox="0 0 927 1200" aria-hidden="false">
    <defs>
      <linearGradient id="photoTone" x1="0" y1="0" x2="1" y2="1">
        <stop offset="0" stop-color="var(--photo-mid)"/>
        <stop offset="0.5" stop-color="var(--photo-dark)"/>
        <stop offset="1" stop-color="var(--photo-light)"/>
      </linearGradient>
    </defs>

    <!-- side pointers -->
    <polygon class="pointer-left" points="0,361 140,408 0,453" fill="var(--slate-soft)"/>
    <polygon class="pointer-right" points="782,782 927,736 927,829" fill="var(--slate-soft)"/>

    <!-- main photo band -->
    <polygon class="photo-band" role="img"
      aria-label="Photo area: athlete gripping a loaded barbell for a deadlift on a gym floor, tinted orange"
      points="0,464 927,167 927,733 0,1030" fill="url(#photoTone)"/>

    <!-- top right accent blocks -->
    <polygon class="accent accent-pale" points="530,254 927,95 927,170 530,344" fill="var(--orange-light)" opacity="0.9"/>
    <polygon class="accent accent-deep" points="787,139 916,130 916,222 787,294" fill="var(--orange)" opacity="0.85"/>
    <polygon class="accent accent-red" points="530,300 787,210 787,294 530,344" fill="var(--red)" opacity="0.6"/>

    <!-- bottom left accent blocks -->
    <polygon class="accent accent-pale" points="0,1060 492,928 492,799 0,967" fill="var(--orange-pale)" opacity="0.92"/>
    <polygon class="accent accent-red" points="0,975 492,799 492,850 0,1015" fill="var(--red)" opacity="0.75"/>
    <polygon class="accent accent-deep" points="106,920 257,870 257,980 106,1051" fill="var(--orange)" opacity="0.85"/>
  </svg>

  <header class="brand">
    <span class="brand-ring"></span>
    <h1 class="brand-name">Veltrano Gym</h1>
    <p class="brand-tagline">Fitter &nbsp;|&nbsp; Stronger &nbsp;|&nbsp; Healthier</p>
  </header>

  <section class="price-badge">
    <p class="price-title">Gym</p>
    <p class="price-subtitle">Membership</p>
    <p class="price-amount">£30</p>
    <p class="price-period">Per Month</p>
  </section>

  <p class="offer">Present this leaflet<br>There will be no joining fee</p>
</main>
</body>
</html>
```